PRojekt: Kartenspiel Seminarspiel für Führungskräfte / Trainerbedarf
Wir sind eine Unternehmensberatung, die Führungskräfte und Unternehmen in Veränderungsprozessen begleitet.
Für Folgende Bestandteile benötige ich ein Design:
Faltschachtel: Format: geschlossen 107 x 21 x 250 mm (Verpackungsdesign)
Druck: 4-farbig + Dispersionslack
Spiel- und Bewertungskarten: Format: 59 x 91 mm Umfang: 60 Karten (5 x 4 Karten / 8 x 5 Karten)
die 5x4 Karten finden sich in dem Word Dokument als Beispiel,
5 Rückseiten mit den vorhanden Logos P, E,R,M, A, aus der Datei KOLVU_Pilot_modell.png
vorderseiten : Texte gemäß der Datei Text_Karten_KOLVU-Pilot-Skat-1.doc
8x 5: 1 Rückseite Bild KOLVU_text0a.png, Vorderseiten: 5 Stück: Text:
1 - 1 Trifft nicht zu
2 - 2 trifft eher nicht zu
3- 3 teils teils
4-4 trifft eher zu
5-5 trifft voll zu
Spielkarten groß : Format: DIN A6
Umfang: 5 Karten pro Set
Rückseite: Bild KOLVU_text0a.png
VOrderseite Text, folgt noch
Spielanleitung Format: DIN A6 (offen DIN A5)
Umfang: 4 Seiten Druck: 4-farbig
Logo zur Verwendung, Anleitung siehe Word-Datei

```html
<!DOCTYPE html>
<html lang="de">
<head>
<meta charset="utf-8">
<title>Spielkarten groß</title>
<link rel="stylesheet" href="https://fonts.googleapis.com/css2?family=Arimo:wght@400;700&display=swap">
<style>
  :root {
    --board-grey: #6f6f6f;
    --card-white: #ffffff;
    --text-dark: #231f20;
    --accent-red: #d91f2f;
    --accent-green: #008a53;
    --accent-blue: #1b72b9;
  }
  html, body {
    margin: 0;
    padding: 0;
    width: 1200px;
    height: 2680px;
    overflow: hidden;
  }
  body {
    background: radial-gradient(ellipse at 50% 40%, #787878 0%, var(--board-grey) 70%, #666 100%);
    font-family: "Arimo", Arial, sans-serif;
    position: relative;
  }
  .board-title {
    position: absolute;
    top: 60px;
    left: 0;
    width: 1254px;
    margin: 0;
    text-align: center;
    color: var(--card-white);
    font-weight: 700;
    font-size: 68px;
    line-height: 1.15;
    letter-spacing: 1px;
  }
  .card {
    position: absolute;
    left: 86px;
    width: 1027px;
    height: 728px;
    background: var(--card-white);
    border-radius: 42px;
    overflow: hidden;
    box-shadow: 0 10px 40px rgba(0,0,0,0.35);
  }
  .card--back { top: 177px; }
  .card--front-red { top: 993px; }
  .card--front-green { top: 1808px; }

  .brand-lockup {
    position: absolute;
    inset: 0;
    display: flex;
    align-items: center;
    justify-content: center;
    gap: 28px;
  }
  .brand-mark {
    width: 56px;
    height: 56px;
    border-radius: 50%;
    background: var(--accent-blue);
  }
  .brand-name {
    font-weight: 400;
    font-size: 84px;
    color: var(--text-dark);
  }

  .card-text {
    position: absolute;
    top: 123px;
    left: 75px;
    margin: 0;
    font-size: 49px;
    line-height: 54.6px;
    color: var(--text-dark);
    white-space: nowrap;
  }
  .card-band {
    position: absolute;
    left: 0;
    bottom: 0;
    width: 1027px;
    height: 101px;
  }
  .band-red { fill: var(--accent-red); }
  .band-green { fill: var(--accent-green); }
</style>
</head>
<body>
  <h1 class="board-title">SPIELKARTEN GROß</h1>

  <section class="card card--back">
    <div class="brand-lockup">
      <span class="brand-mark"></span>
      <span class="brand-name">Kolvu Pilot</span>
    </div>
  </section>

  <section class="card card--front-red">
    <p class="card-text">Lorem ipsum dolor sit amet, consectetur<br>adipiscing elit. Proin tincidunt, lectus id<br>malesuada cursus, lorem augue<br>egestas magna, ut mattis orci ante ut<br>arcu. Sed mauris tellus, fermentum quis<br>ligula nec, posuere pulvinar eros.<br>consequat. Integer consectetur ex vel<br>aliquet iaculis. Vestibulum molestie.</p>
    <svg class="card-band" viewBox="0 0 1027 101" preserveAspectRatio="none" aria-hidden="true">
      <path class="band-red" d="M0 0 Q513 120 1027 0 L1027 101 L0 101 Z"/>
    </svg>
  </section>

  <section class="card card--front-green">
    <p class="card-text">Lorem ipsum dolor sit amet, consectetur<br>adipiscing elit. Proin tincidunt, lectus id<br>malesuada cursus, lorem augue<br>egestas magna, ut mattis orci ante ut<br>arcu. Sed mauris tellus, fermentum quis<br>ligula nec, posuere pulvinar eros.<br>consequat. Integer consectetur ex vel<br>aliquet iaculis. Vestibulum molestie.</p>
    <svg class="card-band" viewBox="0 0 1027 101" preserveAspectRatio="none" aria-hidden="true">
      <path class="band-green" d="M0 0 Q513 120 1027 0 L1027 101 L0 101 Z"/>
    </svg>
  </section>
</body>
</html>
```